Corvimo Business Card

Corvimo is a young and energetic software development consultancy. We spend our time on the road working with clients on their sites an meeting new potential customers and employees!

We need a sharp, vibrant and memorable business card that will inspires those that receive it to look after it as it oozes quality and is a nice thing in its own right.

We like bold colours and distinctive design. So show us what you can do.

In terms of information on the card, it would be good to see:

* Our logo (Obviously :) )
* Employee name
* Email
* Website address
* Mobile number
* Full company name (Corvimo ltd)
* Registered company number
* Registered company address

Industry/Entity Type

Software

Requirements
Nice to have
• We are thinking that having a QR Code on the business card could be a good way of adding active marketing. It would be good to see if you are able to merge the kind of element in to your designs!

Maybe something special could be achieved using a visual QR Code like those produced at http://www.pixoranta.example/ ? You have our media so feel free to have a play.

```html
<!DOCTYPE html>
<html lang="en">
<head>
<meta charset="utf-8">
<title>Corvimo Business Card</title>
<link rel="stylesheet" href="https://fonts.googleapis.com/css2?family=Questrial&display=swap">
<style>
  :root {
    --page: #ffffff;
    --red: #a82020;
    --rail: #ad2222;
    --red-mid: #8c1c1c;
    --maroon: #5c1818;
    --shadow: #2e0a0a;
    --band-grey: #6e5c5c;
    --band-pink: #d9b9b3;
    --texture-light: #b43030;
    --texture-dark: #a82222;
  }
  html, body {
    margin: 0;
    width: 1200px;
    height: 900px;
    overflow: hidden;
    background: var(--page);
  }
  .canvas {
    position: relative;
    width: 1200px;
    height: 900px;
  }
  .card {
    position: absolute;
    left: 0;
    top: 75px;
    width: 1200px;
    height: 720px;
    overflow: hidden;
  }
  .card-art {
    position: absolute;
    inset: 0;
    display: block;
  }
  .brand-name {
    position: absolute;
    left: 655px;
    top: 295px;
    height: 140px;
    display: flex;
    align-items: center;
    margin: 0;
    font-family: "Questrial", sans-serif;
    font-weight: 400;
    font-size: 112px;
    letter-spacing: 2px;
    color: var(--red);
    line-height: 1;
  }
</style>
</head>
<body>
<main class="canvas">
  <section class="card">
    <svg class="card-art" width="1200" height="720" viewBox="0 0 1200 720">
      <defs>
        <linearGradient id="rightFade" x1="0" x2="1" y1="0" y2="0">
          <stop offset="0" stop-color="#000" stop-opacity="0.3"/>
          <stop offset="0.08" stop-color="#000" stop-opacity="0"/>
        </linearGradient>
        <linearGradient id="textureFill" x1="0" y1="0" x2="1" y2="1">
          <stop offset="0" stop-color="var(--texture-light)" stop-opacity="0.7"/>
          <stop offset="0.5" stop-color="var(--texture-light)" stop-opacity="0.9"/>
          <stop offset="1" stop-color="var(--texture-dark)" stop-opacity="0.5"/>
        </linearGradient>
        <filter id="soft" x="-20%" y="-50%" width="140%" height="200%">
          <feGaussianBlur stdDeviation="4"/>
        </filter>
        <filter id="edge" x="-50%" y="-5%" width="200%" height="110%">
          <feGaussianBlur stdDeviation="5"/>
        </filter>
      </defs>

      <!-- panels -->
      <rect class="panel-left" x="0" y="0" width="400" height="720" fill="var(--red)"/>
      <rect class="panel-right" x="398" y="0" width="802" height="720" fill="var(--maroon)"/>
      <rect x="630" y="0" width="570" height="720" fill="url(#rightFade)"/>

      <!-- left panel texture area -->
      <rect class="panel-texture" role="img" aria-label="Soft decorative pattern of overlapping translucent squares"
            x="78" y="120" width="302" height="474" rx="6" fill="url(#textureFill)" filter="url(#soft)"/>

      <!-- name band -->
      <rect class="band-grey" x="398" y="295" width="232" height="140" fill="var(--band-grey)"/>
      <rect class="band-pink" x="630" y="295" width="570" height="140" fill="var(--band-pink)"/>
      <rect x="398" y="436" width="802" height="8" fill="var(--shadow)" opacity="0.35" filter="url(#soft)"/>

      <!-- horizontal rails -->
      <g class="rails">
        <rect x="0" y="104" width="1200" height="8" fill="var(--shadow)" opacity="0.55" filter="url(#soft)"/>
        <rect x="0" y="80" width="1200" height="26" fill="var(--rail)"/>
        <rect x="0" y="639" width="1200" height="8" fill="var(--shadow)" opacity="0.55" filter="url(#soft)"/>
        <rect x="0" y="615" width="1200" height="26" fill="var(--rail)"/>
      </g>

      <!-- vertical bars with soft side shadows -->
      <g class="bar-shadows" fill="var(--shadow)" opacity="0.7" filter="url(#edge)">
        <rect x="404" y="0" width="10" height="720"/>
        <rect x="477" y="0" width="10" height="720"/>
        <rect x="532" y="0" width="10" height="720"/>
        <rect x="578" y="0" width="10" height="720"/>
        <rect x="610" y="0" width="9" height="720"/>
      </g>
      <g class="bars">
        <rect x="412" y="0" width="58" height="720" fill="var(--red)"/>
        <rect x="485" y="0" width="43" height="720" fill="var(--red-mid)"/>
        <rect x="540" y="0" width="32" height="720" fill="var(--red)"/>
        <rect x="586" y="0" width="20" height="720" fill="var(--red-mid)"/>
        <rect x="617" y="0" width="13" height="720" fill="var(--red)"/>
      </g>
    </svg>

    <h1 class="brand-name">Corvimo</h1>
  </section>
</main>
</body>
</html>
```